Tallowmere Consulting Group Business Card Design

We have the logo we just need someone to design a modern business card design.

Name: Leopold Ganzhurt
Phone: 3052918364
Mobile: 9178402297
Web:www.tallowmereconsulting.com
email: lganzhurt@tallowmereconsulting.com
Company: Tallowmere Consulting Group
Title: CEO

Address: 718 Quenby Ave, Miami, Florida 33187

Target Market(s)

companies over 100 employees

Industry/Entity Type

Business

```html
<!DOCTYPE html>
<html lang="en">
<head>
<meta charset="utf-8">
<title>Tallowmere Consulting Group — Business Card</title>
<link href="https://fonts.googleapis.com/css2?family=Open+Sans:wght@400;600&display=swap" rel="stylesheet">
<style>
  :root {
    --stage: #e9e9ec;
    --card-black: #000000;
    --brand-blue: #1f6cf2;
    --ink-white: #ffffff;
    --ink-soft: #d6d6d6;
  }
  * { box-sizing: border-box; margin: 0; padding: 0; }
  html, body {
    width: 1200px; height: 873px; overflow: hidden;
    background: var(--stage);
    font-family: "Open Sans", Arial, sans-serif;
  }
  .stage {
    position: relative; width: 1200px; height: 873px;
    display: flex; align-items: center; justify-content: center; gap: 60px;
  }
  .card {
    position: relative; width: 530px; height: 308px;
    background: var(--card-black); overflow: hidden;
    box-shadow: 0 10px 30px rgba(0,0,0,.25);
  }
  /* Front */
  .front-circle {
    position: absolute; left: -70px; top: -95px;
    width: 250px; height: 250px; border-radius: 50%;
    background: var(--brand-blue);
  }
  .contact {
    position: absolute; left: 36px; top: 150px; color: var(--ink-white);
  }
  .contact-name { font-size: 22px; font-weight: 400; line-height: 1.1; }
  .contact-title { font-size: 9.5px; color: var(--ink-soft); margin: 2px 0 10px; }
  .contact-lines { font-size: 11px; line-height: 1.42; list-style: none; }
  .brand {
    display: flex; align-items: center; gap: 8px; color: var(--ink-white);
  }
  .brand-mark {
    width: 26px; height: 26px; border-radius: 50%; background: var(--ink-white); flex: none;
  }
  .brand-name {
    font-size: 11px; font-weight: 600; letter-spacing: .06em; text-transform: uppercase; line-height: 1.25;
  }
  .front .brand { position: absolute; right: 34px; top: 150px; }
  /* Back */
  .back-band {
    position: absolute; left: 175px; top: 0; width: 190px; height: 100%;
    background: var(--brand-blue);
    display: flex; align-items: center; justify-content: center;
  }
  .back .brand { flex-direction: column; gap: 8px; text-align: center; }
  .back .brand-mark { width: 36px; height: 36px; }
  .back .brand-name { font-size: 12px; }
</style>
</head>
<body>
<main class="stage">
  <section class="card front" aria-label="Business card front">
    <div class="front-circle"></div>
    <div class="contact">
      <h1 class="contact-name">Leopold Ganzhurt</h1>
      <p class="contact-title">Chief Executive Officer</p>
      <ul class="contact-lines">
        <li>718 Quenby Ave.</li>
        <li>Miami, Florida 33187</li>
        <li>Tel.: 3052918364</li>
        <li>Mob.: 9178402297</li>
        <li>lganzhurt@tallowmereconsulting.com</li>
        <li>www.tallowmereconsulting.com</li>
      </ul>
    </div>
    <div class="brand">
      <span class="brand-mark"></span>
      <span class="brand-name">Tallowmere<br>Consulting Group</span>
    </div>
  </section>

  <section class="card back" aria-label="Business card back">
    <div class="back-band">
      <div class="brand">
        <span class="brand-mark"></span>
        <span class="brand-name">Tallowmere<br>Consulting Group</span>
      </div>
    </div>
  </section>
</main>
</body>
</html>
```